Verantix - Solution provider in business consulting

Verantix is a swiss based company providing solutions for developing markets. The business covers various fields of business consulting, such as supply chain, product costs, quality management and manufacturing management. The Business operates in a efficient, straight and solution oriented manner.
The final design should communicate these characteristics. Asian people as well as as western people shall identify the qualities of the company at first sight.
The customer needs business cards with a simple view but an recognizable design, printed in high quality. Engraved elements such as the globe or simple words are possible.
Available colors are: (RAL)
102/102/102
51/102/102
153/204/153
255/102/51
Font: Calibri
Industry/Entity Type
Business
Look and feel
Each slider illustrates characteristics of the customer's brand and the style your logo design should communicate.

```html
<!DOCTYPE html>
<html lang="en">
<head>
<meta charset="utf-8">
<title>Verantix – Business Card</title>
<link href="https://fonts.googleapis.com/css2?family=Carlito:wght@400;700&display=swap" rel="stylesheet">
<style>
  :root {
    --stage: #e8e8e8;
    --grey-dark: #666666;
    --grey-mid: #8a8a8a;
    --silver: #d9d9d9;
    --paper: #ffffff;
    --ink-light: #ffffff;
    --ink-logo: #666666;
  }
  * { margin: 0; padding: 0; box-sizing: border-box; }
  html, body {
    width: 1200px; height: 950px; overflow: hidden;
    background: var(--stage);
    font-family: "Carlito", "Calibri", sans-serif;
  }
  .card {
    position: absolute;
    left: 290px;
    width: 620px; height: 400px;
    overflow: hidden;
    box-shadow: 0 6px 18px rgba(0,0,0,.18);
  }
  /* Contact side */
  .card--front {
    top: 55px;
    background: linear-gradient(112deg, var(--grey-dark) 0%, var(--grey-dark) 46%, #cfcfcf 62%, var(--paper) 78%, #f4f4f4 100%);
  }
  .contact {
    position: absolute; left: 34px; top: 30px;
    color: var(--ink-light);
    font-size: 17px; line-height: 1.25;
  }
  .contact__name { font-size: 27px; font-weight: 700; line-height: 1.1; }
  .contact__role { margin-bottom: 12px; }
  .contact__company { font-weight: 700; }
  .contact__address { margin-bottom: 6px; }
  .contact__line { display: flex; align-items: center; gap: 9px; }
  .contact__line svg { width: 15px; height: 15px; flex: none; fill: var(--ink-light); }
  .globe-art {
    position: absolute;
    left: 150px; top: 170px;
    width: 320px; height: 320px;
    border-radius: 50%;
    background: radial-gradient(circle at 45% 40%, #9a9a9a 0%, #7a7a7a 45%, #f2f2f2 72%, #ffffff 100%);
  }
  .logo {
    display: flex; align-items: center; gap: 10px;
    color: var(--ink-logo);
    font-size: 54px; font-weight: 400; letter-spacing: 1px;
  }
  .logo__dot {
    width: 40px; height: 40px; border-radius: 50%;
    background: var(--grey-dark);
  }
  .logo--vertical {
    position: absolute; left: 560px; top: 200px;
    transform: translate(-50%, -50%) rotate(-90deg);
  }
  /* Brand side */
  .card--back {
    top: 500px;
    background: linear-gradient(160deg, var(--paper) 0%, #f1f1f1 40%, var(--silver) 100%);
    display: flex; flex-direction: column; align-items: center; justify-content: center;
    gap: 18px;
  }
  .card--back .logo { font-size: 64px; }
  .card--back .logo__dot { width: 48px; height: 48px; }
  .web {
    color: var(--grey-mid); font-size: 19px; letter-spacing: .5px;
  }
</style>
</head>
<body>

<section class="card card--front">
  <div class="globe-art" role="img" aria-label="Engraved globe showing East and South-East Asia"></div>

  <div class="contact">
    <div class="contact__name">Marco Feller</div>
    <div class="contact__role">CEO</div>
    <div class="contact__company">Verantix GmbH</div>
    <div class="contact__address">Lindenweg 14, 9000 Talheim<br>Switzerland</div>
    <div class="contact__line">
      <svg viewBox="0 0 16 16" aria-hidden="true"><path d="M2 5c0-2 2-3 6-3s6 1 6 3v1h-3V4.5H5V6H2zM4 7h8l2 6H2z"/></svg>
      +41 71 555 0182
    </div>
    <div class="contact__line">
      <svg viewBox="0 0 16 16" aria-hidden="true"><path d="M4 1h8v14H4zM5.5 2.5v9h5v-9zM7 12.5h2v1H7z" fill-rule="evenodd"/></svg>
      +41 79 555 0347
    </div>
    <div class="contact__line">
      <svg viewBox="0 0 16 16" aria-hidden="true"><path d="M1 3h14v10H1zM2.5 4.5 8 9l5.5-4.5z" fill-rule="evenodd"/></svg>
      marco.feller@verantix.ch
    </div>
    <div class="contact__line">
      <svg viewBox="0 0 16 16" aria-hidden="true"><circle cx="8" cy="8" r="7"/><path d="M5 5c2 0 2 2 4 2s1 3-1 3-2 2-3 1 0-3-1-4 0-2 1-2z" fill="#666"/></svg>
      www.verantix.ch
    </div>
  </div>

  <div class="logo logo--vertical">
    <span class="logo__dot"></span><span class="logo__name">verantix</span>
  </div>
</section>

<section class="card card--back">
  <div class="logo">
    <span class="logo__dot"></span><span class="logo__name">verantix</span>
  </div>
  <div class="web">www.verantix.ch</div>
</section>

</body>
</html>
```